PowerPoint Design Project

Design Brief
Corvanta is updating its stationary templates to reflect the company’s position as market leader in smart-location based solutions.
Using the existing Corvanta logo and corporate colours, create an engaging and visually appealing PowerPoint presentation template identity that works when printed on A4 and US Letter sized paper.
The successful designs will complement the current look and feel of the Corvanta website (www.corvanta-example.net) and communicate that Corvanta is a dynamic and modern technology company that is at the cutting edge of innovation.
Corvanta Brand
Corvanta stands for Precision Location Technology. The brand represents both a unique, highly innovative platform product and a mature consulting and support organisation dedicated to delivering solutions to blue-chip customer problems. The orange colour implies creativity while blue evokes trust and a rational approach. “Cor” is Latin and means “where”, so the brand directly addresses the focus of the company: location. “Sense” can mean that we have sensing technology to support our precision location aware applications and solutions, but also that we make sensible use of location data to improve customer processes.
Corvanta Corporate Profile
Corvanta is a market leader of location-based Smart Factory Solutions which enables companies to optimise their business processes. By keeping track of key assets, Corvanta solutions bring clarity to complex operations in industries while also improving quality and reliability. Corvanta uses a unique combination of advancefd industry knowledge and an experienced team to deliver effective and superior solutions that offer unprecedented visibility, control and accuracy, delivering time and cost savings. Corvanta solutions are easy to implement and flexible to a particular business’s needs, no matter which area of the globe they operate in.
Corvanta offers two location-oriented products; RTLS (Real-time Location Solutions) and Geospatial Systems and operates in a number of industries ranging from manufacturing and utilities to telecommunications and is used by a number of blue chip customers across the world, such as KLT, Skyvane, Dromtrack, Pellow Power, RIM and Nordfeld Fernmelde.
Corvanta Corporate Colours
Orange:
Pantone 021C
R: 237 / G: 110 / B: 0
C: 0 / M: 53 / Y: 100 / K: 0
Hex #ED6E00
Dark Blue:
Pantone 662C
R: 15 / G: 31 / B: 122
C: 100 / M: 71 / Y: 0 / K:0
Hex #0F1F7A
Light Blue:
Pantone 300C
R: 0 / G: 110 / B: 199
C: 100 / M: 44 / Y: 0 / K:0
Hex #006EC7
Corvanta Corporate Fonts
The preferred font is Tahoma for Title, Topics and Print. In certain situations, Arial is an acceptable alternative.
Target Market(s)
Manufacturing industry, Automotive and Aerospace
Industry/Entity Type
Telecommunications
Look and feel
Each slider illustrates characteristics of the customer's brand and the style your logo design should communicate.

```html
<!DOCTYPE html>
<html lang="en">
<head>
<meta charset="utf-8">
<title>Corvanta – Presentation Title Slide</title>
<link rel="stylesheet" href="https://fonts.googleapis.com/css2?family=Noto+Sans:wght@400;700&display=swap">
<style>
  :root {
    --cream-top: #efede2;
    --cream-bottom: #f8f6ee;
    --charcoal: #333037;
    --charcoal-deep: #2d2a31;
    --divider: #5b5860;
    --heading: #3a3a3a;
    --body-grey: #7a7a7a;
    --accent-yellow: #ffae00;
    --contact-yellow: #f6b400;
    --brand-text: #f2f0e8;
    --link-blue: #2a3cff;
    --white: #ffffff;
  }
  * { margin: 0; padding: 0; box-sizing: border-box; }
  html, body {
    width: 1200px;
    height: 900px;
    overflow: hidden;
    background: var(--charcoal);
  }
  .slide {
    position: relative;
    width: 1200px;
    height: 900px;
    font-family: "Noto Sans", Tahoma, Arial, sans-serif;
  }
  .title-area {
    position: absolute;
    left: 0; top: 0;
    width: 1200px;
    height: 495px;
    background: linear-gradient(180deg, var(--cream-top) 0%, var(--cream-bottom) 100%);
    border-bottom: 2px solid var(--divider);
  }
  .title {
    position: absolute;
    left: 64px;
    top: 92px;
    color: var(--heading);
    font-weight: 700;
  }
  .title-main {
    display: block;
    font-size: 84px;
    line-height: 88px;
    letter-spacing: -1px;
  }
  .title-sub {
    display: block;
    font-size: 54px;
    line-height: 54px;
    margin-top: -8px;
    letter-spacing: 0;
  }
  .intro {
    position: absolute;
    left: 82px;
    top: 246px;
    width: 516px;
    font-size: 18px;
    line-height: 24px;
    color: var(--body-grey);
    text-align: justify;
  }
  .footer-area {
    position: absolute;
    left: 0; top: 497px;
    width: 1200px;
    height: 379px;
    background: radial-gradient(ellipse at 50% 120%, #3a3740 0%, var(--charcoal) 55%, var(--charcoal-deep) 100%);
  }
  .brand-name {
    position: absolute;
    left: 66px;
    top: 770px;
    font-size: 42px;
    line-height: 48px;
    font-weight: 700;
    color: var(--brand-text);
  }
  .contact {
    position: absolute;
    left: 892px;
    top: 769px;
    font-size: 15px;
    line-height: 19px;
    color: var(--white);
    font-style: normal;
  }
  .contact-heading {
    font-weight: 700;
    color: var(--contact-yellow);
  }
  .contact a {
    color: var(--link-blue);
    text-decoration: underline;
  }
  .accent-band {
    position: absolute;
    left: 0; top: 876px;
    width: 1200px;
    height: 24px;
    background: var(--accent-yellow);
  }
</style>
</head>
<body>
  <main class="slide">
    <section class="title-area">
      <h1 class="title">
        <span class="title-main">Presentation</span>
        <span class="title-sub">Heading comes here</span>
      </h1>
      <p class="intro">Lorem Ipsum is simply dummy text of the printing and typesetting industry. Lorem Ipsum has been the industry's standard dummy text ever</p>
    </section>

    <section class="footer-area"></section>

    <div class="brand-name">Corvanta</div>

    <address class="contact">
      <div class="contact-heading">Contact Us</div>
      <div>Lorem ipsum&nbsp; State, Country</div>
      <div>P.&nbsp; 281 555 0142/ <a href="#">info@sample.net</a></div>
    </address>

    <div class="accent-band"></div>
  </main>
</body>
</html>
```